Military Cadence Catalog

Hi Piers,
In regards to transitioning Halvern Recordings to Quillmere will consist of numerous legal decisions. Of great significance is whether to use Quillmere as a "Doing Business As" under Halvern Recordings or whether to actually create a new business called Quillmere and to transfer all copyright registrations to this new company.
The "Coming Soon" page is crucial in that it provides me the opportunity to legally address, and sue, companies that have created products which are exact replicas of our cadence recordings.
Attached is a link to a company who has pirated our recordings.
Thus I was wondering if you think we should quietly release the catalog under Halvern Recordings based on HR having copyrights for every product. Once we have addressed all the piracy and copyright infringement against HR, then we can have the high profile re-launch of the catalog under Quillmere.

```html
<!DOCTYPE html>
<html lang="en">
<head>
<meta charset="utf-8">
<title>Quillmere — Military Cadence Catalog</title>
<link href="https://fonts.googleapis.com/css2?family=Black+Ops+One&family=Montserrat:wght@300;400;500;600;700;800&display=swap" rel="stylesheet">
<style>
:root{
  --red:#a30b0b;
  --red-bright:#f00d0d;
  --navy:#13152d;
  --sage:#4f5f57;
  --ink:#1a1a1a;
  --white:#ffffff;
}
*{box-sizing:border-box;margin:0;padding:0}
html,body{width:1200px;height:3434px;overflow:hidden;background:var(--white)}
body{position:relative;font-family:"Montserrat",sans-serif;color:var(--ink)}
.abs{position:absolute}
.display{font-family:"Black Ops One",sans-serif;text-transform:uppercase;letter-spacing:.5px}
.btn{position:absolute;display:flex;align-items:center;justify-content:center;color:var(--white);font-size:16px;font-weight:500;background:var(--red)}
.btn--navy{background:var(--navy)}
.btn--sage{background:var(--sage)}

/* hero */
.hero{left:0;top:0;width:1200px;height:645px;background:linear-gradient(120deg,#4a4a38 0%,#2f3222 35%,#3b2c26 60%,#5a4a40 80%,#2d2a22 100%)}
.hero__shade{left:0;top:0;width:1200px;height:645px;background:rgba(10,10,10,.35)}
.logo{font-family:"Montserrat",sans-serif;font-weight:800;color:var(--red-bright);font-size:28px;letter-spacing:.5px}
.hero .logo{left:160px;top:14px}
.menu{left:1020px;top:19px}
.hero__title{left:150px;top:248px;width:900px;text-align:center;color:var(--white);font-size:42px;line-height:54px}
.hero__lede{left:250px;top:358px;width:700px;text-align:center;color:var(--white);font-size:16.5px;font-weight:500;line-height:23px}

/* story */
.story__title{left:143px;top:718px;width:400px;text-align:center;font-size:28px}
.story__kicker{left:143px;top:775px;width:400px;text-align:center;color:var(--red);font-size:17px;font-weight:500}
.story__text{left:153px;top:826px;width:380px;text-align:center;font-size:16.5px;line-height:22.5px}
.story__photo{left:596px;top:709px;width:431px;height:355px;background:linear-gradient(160deg,#cfc6b3,#8b7f6a 55%,#4a4236)}
.story__accent{left:609px;top:725px;width:431px;height:355px;background:var(--red-bright)}
.frame{position:absolute;inset:10px;border:1px solid rgba(255,255,255,.7)}

/* branches */
.branches{left:0;top:1171px;width:1200px;height:549px;background:var(--navy)}
.branches__title{left:0;top:1242px;width:1200px;text-align:center;color:var(--white);font-size:29px}
.branches__kicker{left:0;top:1290px;width:1200px;text-align:center;color:var(--red);font-size:16.5px;font-weight:500}
.card{position:absolute;top:1348px;width:280px;height:421px}
.card__img{position:absolute;left:0;top:0;width:280px;height:348px}
.card__label{position:absolute;left:0;top:348px;width:280px;height:73px;background:var(--sage);color:var(--white);text-align:center;padding-top:13px}
.card__name{font-size:20px;font-weight:500;line-height:24px}
.card__tags{font-size:10px;font-weight:500;margin-top:3px;letter-spacing:.2px}
.card__tag-flag{position:absolute;left:9px;top:12px;height:24px;width:128px;background:var(--red);color:var(--white);font-size:10px;padding:6px 0 0 22px;clip-path:polygon(0 0,100% 0,88% 100%,0 100%)}
.card .frame{bottom:auto;height:324px}

/* listen */
.listen__title{left:0;top:1920px;width:1200px;text-align:center;font-size:29px}
.listen__kicker{left:0;top:1966px;width:1200px;text-align:center;color:var(--red);font-size:17px;font-weight:500}
.listen__text{left:0;top:2006px;width:1200px;text-align:center;font-size:16.5px}
.video{left:225px;top:2135px;width:751px;height:342px;background:linear-gradient(135deg,#b5513d,#d88d72 35%,#a1432f 60%,#6b2a1d)}
.video__play{left:564px;top:2251px;width:72px;height:72px;border-radius:50%;background:rgba(40,30,50,.55)}
.video__bar{left:245px;top:2453px;width:711px;height:2px;background:rgba(255,255,255,.5)}

/* stats */
.stats{left:0;top:2627px;width:1200px;height:336px;background:linear-gradient(100deg,#2a1628,#3a1b22 40%,#4a1f1c 70%,#2b1726)}
.stat{position:absolute;top:2738px;width:240px;text-align:center;color:var(--white)}
.stat__num{font-size:52px;font-weight:700;line-height:60px}
.stat__label{font-size:16px;font-weight:700;margin-top:2px}

/* call to action */
.cta{left:0;top:2963px;width:1200px;height:181px;background:var(--sage)}
.cta__title{left:157px;top:2990px;color:var(--white);font-size:33px;font-weight:300}
.cta__text{left:158px;top:3038px;width:420px;color:var(--white);font-size:16px;line-height:22.5px}

/* footer */
.footer{left:0;top:3144px;width:1200px;height:290px;background:var(--navy)}
.footer .logo{left:153px;top:3188px}
.footer__col{position:absolute;top:3190px;list-style:none;color:var(--white);font-size:19px;line-height:37.5px}
.footer__legal{position:absolute;top:3395px;color:var(--white);font-size:12px}
</style>
</head>
<body>

<!-- hero -->
<section class="abs hero" role="img" aria-label="Photo of uniformed troops in helmets marching in formation before a waving national flag"></section>
<div class="abs hero__shade"></div>
<div class="abs logo">QUILLMERE.COM</div>
<svg class="abs menu" width="20" height="16" viewBox="0 0 20 16" aria-label="Menu">
  <g stroke="#fff" stroke-width="1.5"><line x1="0" y1="2" x2="20" y2="2"/><line x1="0" y1="8" x2="20" y2="8"/><line x1="0" y1="14" x2="20" y2="14"/></g>
</svg>
<h1 class="abs display hero__title">Authentic Military Cadences Recorded Live with U.S. Troops</h1>
<p class="abs hero__lede">Experience the energy, discipline, and tradition of military training through one of the largest military cadence collections ever recorded.</p>
<a class="btn btn--navy" style="left:356px;top:429px;width:236px;height:56px">Browse Collection</a>
<a class="btn" style="left:607px;top:429px;width:236px;height:56px">Listen to a Sample</a>

<!-- story -->
<h2 class="abs display story__title">The Quillmere Story</h2>
<p class="abs story__kicker">Preserving Military Tradition</p>
<div class="abs story__text">
  <p>Recorded live during military PT training, these authentic cadence recordings capture the voices, motivation, and spirit of America's Armed Forces.</p>
  <p style="margin-top:22px">A father-and-son project dedicated to preserving military heritage through sound.</p>
</div>
<a class="btn" style="left:223px;top:1013px;width:237px;height:55px">Learn More</a>
<div class="abs story__accent"></div>
<div class="abs story__photo" role="img" aria-label="Sepia archival photo of soldiers marching and cheering beneath a raised flag"><div class="frame"></div></div>

<!-- branches -->
<section class="abs branches"></section>
<h2 class="abs display branches__title">Explore by Branch</h2>
<p class="abs branches__kicker">Choose Your Collection</p>

<div class="card" style="left:160px">
  <div class="card__img" role="img" aria-label="Silhouettes of marines walking toward a bright hazy sky" style="background:linear-gradient(180deg,#5a5a4a,#d8d2b8 35%,#4b4a40 65%,#15161a)"><div class="frame"></div></div>
  <div class="card__tag-flag">Shop on Tunehall</div>
  <div class="card__label"><div class="card__name">U.S MARINE CORPS</div><div class="card__tags">RUNNING • MARCHING • PERCUSSION</div></div>
</div>
<div class="card" style="left:460px">
  <div class="card__img" role="img" aria-label="Columns of army soldiers in camouflage marching under a flag and blue sky" style="background:linear-gradient(180deg,#4f6d93,#a8b7c6 35%,#8a7b62 65%,#5e5342)"><div class="frame"></div></div>
  <div class="card__label"><div class="card__name">ARMY</div><div class="card__tags">RUNNING • MARCHING</div></div>
</div>
<div class="card" style="left:760px">
  <div class="card__img" role="img" aria-label="Silhouetted paratroopers beneath a flag against an orange sunset" style="background:linear-gradient(180deg,#5b2a1e,#c4551e 40%,#f2a13a 62%,#2a1710)"><div class="frame"></div></div>
  <div class="card__label"><div class="card__name">AIRBORNE</div><div class="card__tags">RUNNING • MARCHING</div></div>
</div>

<a class="btn" style="left:481px;top:1803px;width:238px;height:54px">View All Collections</a>

<!-- listen -->
<h2 class="abs display listen__title">Listen Before You Buy</h2>
<p class="abs listen__kicker">Hear the Difference</p>
<p class="abs listen__text">Experience authentic military cadence recordings before purchasing.</p>
<a class="btn btn--sage" style="left:225px;top:2060px;width:238px;height:55px">Real voices</a>
<a class="btn btn--sage" style="left:481px;top:2060px;width:238px;height:55px">Real troops</a>
<a class="btn btn--sage" style="left:737px;top:2060px;width:238px;height:55px">Real training</a>
<div class="abs video" role="img" aria-label="Video still of soldiers advancing with rifles in front of a flag, tinted red"></div>
<div class="abs video__play"></div>
<svg class="abs" style="left:588px;top:2276px" width="24" height="24" viewBox="0 0 24 24" aria-label="Play"><polygon points="4,2 22,12 4,22" fill="#d20f0f"/></svg>
<div class="abs video__bar"></div>
<a class="btn" style="left:481px;top:2501px;width:238px;height:55px">Listen to Samples</a>

<!-- stats -->
<section class="abs stats" role="img" aria-label="Darkened background of soldiers in formation before a flag"></section>
<div class="stat" style="left:143px"><div class="stat__num">32</div><div class="stat__label">Albums</div></div>
<div class="stat" style="left:343px"><div class="stat__num">3</div><div class="stat__label">Cadence Series</div></div>
<div class="stat" style="left:557px"><div class="stat__num">7</div><div class="stat__label">Military Categories</div></div>
<div class="stat" style="left:801px"><div class="stat__num">100%</div><div class="stat__label">Authentic Recordings</div></div>

<!-- call to action -->
<section class="abs cta"></section>
<h2 class="abs cta__title">Keep Military Tradition Alive</h2>
<p class="abs cta__text">Explore authentic military cadence recordings and discover the sounds that motivated generations of service members.</p>
<a class="btn" style="left:609px;top:3021px;width:206px;height:56px">Browse Catalog</a>
<a class="btn" style="left:835px;top:3021px;width:205px;height:56px">Purchase on Tunehall</a>

<!-- footer -->
<footer class="abs footer"></footer>
<div class="abs logo">QUILLMERE.COM</div>
<ul class="footer__col" style="left:479px"><li>Home</li><li>Catalog</li><li>Marine Corps</li><li>Army</li><li>Airborne</li></ul>
<ul class="footer__col" style="left:713px"><li>Rangers</li><li>Navy</li><li>Air Force</li><li>Contact</li></ul>
<ul class="footer__col" style="left:932px;top:3192px"><li>Friendwall</li><li>Photoline</li><li>Clipstream</li></ul>
<p class="footer__legal" style="left:160px">© 2026 | www.quillmere.com</p>
<p class="footer__legal" style="left:746px">Licensing Information &nbsp;&nbsp; | &nbsp;&nbsp; Terms &amp; Conditions</p>
<p class="footer__legal" style="left:1117px;top:3391px">M1</p>

</body>
</html>
```